Business Card Design for Occupational Medicine Start Up Company

We need to design a professional business card. We are a healthcare company providing occupational medicine services to blue collar industries. We are professional, efficient and high quality service providers.

Target Market(s)

Blue Collar Industry: Shipbuilding, Ports, Trucking Companies; The Executives and Safety Officers for these companies

Industry/Entity Type

Healthcare

Contact Information for Business Card

Logo, Name, Title, Email, Phone

Other font styles liked:
• Please match our Brand Guide

Requirements
Must have
• Our Company Colors and Logo

```html
<!DOCTYPE html>
<html lang="en">
<head>
<meta charset="utf-8">
<title>CrewWell Business Card</title>
<link href="https://fonts.googleapis.com/css2?family=Montserrat:wght@500;700&family=Arimo:wght@400;700&display=swap" rel="stylesheet">
<style>
  :root {
    --navy: #2b3190;
    --navy-deep: #232a7e;
    --sky: #1aa9e6;
    --amber: #f3a52b;
    --paper: #ffffff;
    --ink: #333333;
    --backdrop: #e9eaee;
  }
  * { margin: 0; padding: 0; box-sizing: border-box; }
  html, body { width: 1200px; height: 900px; overflow: hidden; }
  body {
    background: var(--backdrop);
    font-family: "Arimo", Arial, sans-serif;
    position: relative;
  }
  .card {
    position: absolute;
    left: 270px;
    width: 660px;
    height: 377px;
    border-radius: 30px;
    overflow: hidden;
    box-shadow: 0 10px 30px rgba(20, 25, 60, 0.18);
  }
  .card-front { top: 52px; background: var(--paper); }
  .card-back { top: 471px; background: var(--navy); }

  .brand {
    position: absolute;
    display: flex;
    align-items: center;
    gap: 12px;
  }
  .brand-dot { border-radius: 50%; }
  .brand-name {
    font-family: "Montserrat", sans-serif;
    font-weight: 700;
    letter-spacing: 1px;
  }
  .card-front .brand { left: 44px; top: 36px; }
  .card-front .brand-dot { width: 30px; height: 30px; background: var(--amber); }
  .card-front .brand-name { font-size: 26px; color: var(--navy); }

  .card-back .brand { left: 50%; top: 50%; transform: translate(-50%, -50%); gap: 18px; }
  .card-back .brand-dot { width: 46px; height: 46px; background: var(--sky); }
  .card-back .brand-name { font-size: 44px; color: var(--paper); }

  .holder {
    position: absolute;
    right: 48px;
    top: 120px;
    text-align: right;
  }
  .holder-name {
    font-family: "Montserrat", sans-serif;
    font-weight: 700;
    font-size: 30px;
    color: var(--navy);
    letter-spacing: 0.5px;
  }
  .holder-name .surname { color: var(--sky); }
  .holder-title { font-size: 17px; color: var(--ink); margin-top: 4px; }

  .divider {
    position: absolute;
    left: 150px;
    right: 40px;
    top: 196px;
    height: 2px;
    background: var(--amber);
  }

  .contacts {
    position: absolute;
    left: 44px;
    top: 212px;
    list-style: none;
    font-size: 15px;
    color: var(--ink);
  }
  .contacts li { display: flex; align-items: center; gap: 8px; line-height: 23px; }
  .contacts svg { width: 12px; height: 12px; flex: none; }

  .footer-band { position: absolute; left: 0; bottom: 0; width: 660px; height: 80px; display: block; }
  .address {
    position: absolute;
    left: 30px;
    bottom: 24px;
    width: 270px;
    font-size: 14px;
    line-height: 18px;
    white-space: nowrap;
    color: var(--paper);
  }
</style>
</head>
<body>

<section class="card card-front" aria-label="Business card front">
  <div class="brand">
    <span class="brand-dot"></span>
    <span class="brand-name">CREWWELL</span>
  </div>

  <div class="holder">
    <div class="holder-name">DANIEL <span class="surname">BROOKS</span></div>
    <div class="holder-title">CEO/Founder</div>
  </div>

  <div class="divider"></div>

  <ul class="contacts">
    <li>
      <svg viewBox="0 0 12 12"><circle cx="6" cy="6" r="6" fill="var(--sky)"/><path d="M3.6 3.2l1.2-.4.8 1.6-.7.6a4 4 0 0 0 2 2l.6-.7 1.6.8-.4 1.2C6.6 8.6 3.4 5.4 3.6 3.2z" fill="#fff"/></svg>
      555-014-2290
    </li>
    <li>
      <svg viewBox="0 0 12 12"><rect x="0.5" y="2" width="11" height="8" rx="1" fill="var(--sky)"/><path d="M1 2.6L6 6.6l5-4" stroke="#fff" stroke-width="1" fill="none"/></svg>
      hello@crewwellhealth.com
    </li>
    <li>
      <svg viewBox="0 0 12 12"><circle cx="6" cy="6" r="6" fill="var(--sky)"/><path d="M6 0.5v11M0.5 6h11M6 0.5c-3 3-3 8 0 11M6 0.5c3 3 3 8 0 11" stroke="#fff" stroke-width="0.8" fill="none"/></svg>
      www.crewwellhealth.com
    </li>
  </ul>

  <svg class="footer-band" viewBox="0 0 660 80" aria-hidden="true">
    <path d="M0 16 H296 Q314 16 320 34 L332 72 H660 V80 H0 Z" fill="var(--navy)"/>
    <path d="M326 56 H436 L442 70 H331 Z" fill="var(--sky)"/>
    <path d="M444 56 H552 L558 70 H450 Z" fill="var(--navy-deep)"/>
    <path d="M560 56 H660 V70 H566 Z" fill="var(--amber)"/>
  </svg>
  <div class="address">2150 Harbor Line Road Country, AB 10245</div>
</section>

<section class="card card-back" aria-label="Business card back">
  <div class="brand">
    <span class="brand-dot"></span>
    <span class="brand-name">CREWWELL</span>
  </div>
</section>

</body>
</html>
```